2 websites needed.

2 websites needed, 3 pages deep. one from cat perspective, one from dog perspective. will pull in news from news sites and anthropomorphize it. News styles will be given similar to "The Sprocket", Glintwire, etc
These websites are for a game set in a world called Velurindale where cats live and dogs from Quendrosa in the Zellam Concord are their enemies. Velurindale colors are purple/blues and greens, Quendrosa - red/black. They are led by General Pikewhistle and his army of robot rats and hamsters. The Quendrosa paper should be ruggeed, big fonts, strong type and large "shouting" type letters. Velurindale should be delicate, sweet and feminine... The news being reported will be human current news but anthropomorphized to be told by cats or dogs depending on the perspective...cats are left-leaning, dogs alt-right. Sans Serif font for Quendrosan paper, Serif for The Morning Quill.
Target Market(s)
18-36
Industry/Entity Type
media/gaming
Coding
Coded - Design and coding required

```html
<!DOCTYPE html>
<html lang="en">
<head>
<meta charset="utf-8">
<title>Velurindale</title>
<link rel="stylesheet" href="https://fonts.googleapis.com/css2?family=Playfair+Display:wght@500;600&family=Plus+Jakarta+Sans:wght@400;500;600;700&display=swap">
<style>
:root{
  --page:#f3f4fa;
  --band:#e8ebf7;
  --ink:#1d1b2e;
  --muted:#5d5f6e;
  --soft:#8a8c99;
  --accent:#e23b3b;
  --blue:#4448e2;
  --blue-deep:#3438c8;
  --line:#d8dae6;
  --white:#ffffff;
}
*{box-sizing:border-box;margin:0;padding:0}
html,body{width:1200px;height:5068px;overflow:hidden}
body{background:var(--page);font-family:"Plus Jakarta Sans",Arial,sans-serif;color:var(--ink);position:relative}
.abs{position:absolute}
.display{font-family:"Playfair Display",Georgia,serif;font-weight:600;letter-spacing:0}
a{color:inherit;text-decoration:none}

/* header */
.menu-btn{left:85px;top:38px;width:24px}
.menu-btn span{display:block;height:2px;background:var(--ink);margin-bottom:6px}
.logo{left:0;width:1200px;top:22px;text-align:center;font-size:46px;line-height:64px;font-weight:600}
.header-social{left:884px;top:40px;display:flex;gap:22px;font-size:11px;color:var(--muted);align-items:center}
.header-social span{display:flex;align-items:center;gap:5px}
.header-social i{width:9px;height:9px;border-radius:50%;background:var(--ink);display:block}
.search-btn{left:1073px;top:34px;width:38px;height:38px;border-radius:50%;background:var(--blue);display:flex;align-items:center;justify-content:center;box-shadow:0 0 0 5px #dfe0fb}
.main-nav{left:0;width:1200px;top:116px;display:flex;justify-content:center;gap:42px;font-size:12.5px;font-weight:600}
.main-nav a{display:flex;align-items:center;gap:4px;padding-bottom:8px}
.main-nav a.active{color:var(--accent);border-bottom:2px solid var(--accent)}

/* hero */
.hero-card{border-radius:18px;overflow:hidden;color:var(--white)}
.hero-card .shade{position:absolute;inset:0;background:linear-gradient(180deg,rgba(0,0,0,0) 40%,rgba(0,0,0,.7) 100%)}
.tag{display:inline-block;background:var(--accent);color:var(--white);font-size:10px;font-weight:700;letter-spacing:.6px;padding:4px 8px;border-radius:3px;text-transform:uppercase}
.hero-text{position:absolute;left:56px;bottom:36px}
.hero-text h2{font-size:38px;line-height:50px;margin-top:12px}
.side-text{position:absolute;left:20px;bottom:18px}
.side-text h3{font-size:24px;line-height:36px;margin-top:10px}

/* section headings */
.section-title{font-size:38px;line-height:50px}
.dash{display:flex;gap:5px;margin-top:8px}
.dash b{height:3px;width:24px;background:var(--accent)}
.dash i{height:3px;width:3px;background:var(--accent)}
.center .dash{justify-content:center}
.link-more{font-size:13px;font-weight:600;color:var(--blue);border-bottom:1px solid var(--blue);padding-bottom:2px}

/* trending */
.topics{left:85px;top:854px;display:flex;gap:12px}
.topic{width:248px;height:374px;border-radius:16px;position:relative;overflow:hidden}
.topic .shade{position:absolute;inset:0;background:linear-gradient(180deg,rgba(0,0,0,0) 60%,rgba(0,0,0,.55) 100%)}
.topic span{position:absolute;left:0;right:0;bottom:34px;text-align:center;color:var(--white);font-size:19px}

/* articles */
.articles{left:85px;top:1418px;width:1028px;display:grid;grid-template-columns:504px 504px;column-gap:20px;row-gap:0}
.article{text-align:center;height:693px}
.article .photo{height:378px;border-radius:16px;position:relative;overflow:hidden}
.stats{position:absolute;right:28px;top:26px;background:var(--blue);color:var(--white);border-radius:12px;padding:4px 10px;display:flex;gap:10px;font-size:10px;font-weight:600}
.stats span{display:flex;align-items:center;gap:3px}
.cats{margin-top:16px;font-size:10px;letter-spacing:1px;color:var(--muted);font-weight:500}
.cats i{margin:0 10px;font-style:normal}
.article h3{font-size:21px;line-height:31px;margin:10px 20px 0}
.byline{display:flex;align-items:center;justify-content:center;gap:8px;font-size:11px;color:var(--muted);margin-top:10px;letter-spacing:.3px}
.avatar{width:26px;height:26px;border-radius:50%;background:linear-gradient(135deg,#caa08a,#8c5c49)}
.excerpt{font-size:14.5px;line-height:26px;color:var(--muted);margin:14px 16px 0}
.article .link-more{display:inline-block;margin-top:26px}
.btn{display:inline-flex;align-items:center;justify-content:center;background:var(--blue);color:var(--white);font-weight:600;font-size:14px;border-radius:24px}
.divider{left:85px;top:2931px;width:1028px;height:1px;background:var(--line)}

/* card rows */
.card-row{left:85px;width:1028px;display:flex;gap:28px}
.post{width:324px}
.post .photo{height:256px;border-radius:12px}
.meta{font-size:10px;color:var(--blue);margin-top:18px;letter-spacing:.4px}
.post h3{font-size:21px;line-height:30px;margin-top:10px}
.post p{font-size:15px;line-height:25px;color:var(--muted);margin-top:14px}
.post .btn{width:151px;height:44px;margin-top:24px}
.post .link-more{display:inline-block;margin-top:22px;font-weight:500}
.explore-band{left:0;top:3710px;width:1200px;height:700px;background:var(--band)}

/* newsletter */
.newsletter{left:104px;top:4475px;width:986px;height:210px;background:var(--blue-deep);border-radius:10px;color:var(--white)}
.newsletter h2{position:absolute;left:44px;top:58px;font-size:32px;line-height:44px}
.subscribe{position:absolute;left:512px;top:82px;display:flex;height:44px}
.subscribe .field{width:287px;background:var(--white);color:var(--soft);font-size:12px;display:flex;align-items:center;gap:6px;padding-left:12px}
.subscribe .send{width:124px;background:var(--blue);color:var(--white);font-weight:700;font-size:14px;display:flex;align-items:center;justify-content:center}

/* footer */
.foot-logo{left:85px;top:4778px;font-size:44px;line-height:60px}
.foot-about{left:85px;top:4855px;width:290px;font-size:13.5px;line-height:26px;color:var(--muted)}
.copy{left:85px;top:4944px;font-size:12.5px;color:var(--muted)}
.copy b{color:var(--blue)}
.stamp{left:85px;top:4968px;font-size:10px;color:var(--soft)}
.foot-col h4{font-family:"Playfair Display",Georgia,serif;font-weight:600;font-size:18px}
.foot-col ul{list-style:none;margin-top:22px;font-size:13.5px;color:var(--muted)}
.foot-col li{height:30px}
.follow{left:846px;top:4851px;display:grid;grid-template-columns:130px 130px;gap:9px 8px}
.follow a{height:60px;border:1px solid var(--line);border-radius:4px;display:flex;flex-direction:column;align-items:center;justify-content:center;gap:6px;font-size:13px;color:var(--muted)}
.follow a i{width:10px;height:10px;border-radius:50%;background:var(--ink)}
</style>
</head>
<body>

<!-- header -->
<div class="abs menu-btn" aria-label="Menu"><span></span><span></span><span></span></div>
<div class="abs logo display">Velurindale</div>
<div class="abs header-social">
  <span><i></i>2K</span><span><i></i>1K</span><span><i></i>890</span>
</div>
<div class="abs search-btn">
  <svg width="16" height="16" viewBox="0 0 16 16" fill="none" stroke="#fff" stroke-width="2"><circle cx="7" cy="7" r="5"/><path d="M11 11l3.5 3.5" stroke-linecap="round"/></svg>
</div>
<nav class="abs main-nav">
  <a class="active" href="#">HOME</a>
  <a href="#">ARCHIVES</a>
  <a href="#">POSTS</a>
  <a href="#">POST FORMAT <svg width="9" height="6" viewBox="0 0 9 6" fill="none" stroke="#1d1b2e" stroke-width="1.4"><path d="M1 1l3.5 3.5L8 1"/></svg></a>
  <a href="#">PAGES <svg width="9" height="6" viewBox="0 0 9 6" fill="none" stroke="#1d1b2e" stroke-width="1.4"><path d="M1 1l3.5 3.5L8 1"/></svg></a>
</nav>

<!-- hero -->
<article class="abs hero-card" style="left:85px;top:157px;width:700px;height:500px;background:radial-gradient(circle at 65% 30%,#a8442f 0%,#3b2622 45%,#141112 100%)" role="img" aria-label="Tabby cat sitting by a computer in red light">
  <div class="shade"></div>
  <div class="hero-text">
    <span class="tag">Lifestyle</span>
    <h2 class="display">The Whisker Council opens<br>new sunbeam parks for all</h2>
  </div>
</article>
<article class="abs hero-card" style="left:799px;top:157px;width:314px;height:240px;background:linear-gradient(135deg,#6c7be0 0%,#b59dcb 50%,#d7a89e 100%)" role="img" aria-label="Kitten sitting in front of a colourful backdrop">
  <div class="shade"></div>
  <div class="side-text"><span class="tag">Lifestyle</span><h3 class="display">Kitten choir wins the<br>spring harmony prize</h3></div>
</article>
<article class="abs hero-card" style="left:799px;top:415px;width:314px;height:242px;background:linear-gradient(160deg,#b07a5c 0%,#6d4a3c 55%,#2e2420 100%)" role="img" aria-label="Close-up of a tabby cat looking up">
  <div class="shade"></div>
  <div class="side-text"><span class="tag">Lifestyle</span><h3 class="display">Yarn markets rally<br>after a gentle week</h3></div>
</article>

<!-- trending topics -->
<div class="abs" style="left:85px;top:762px">
  <h2 class="section-title display">Trending Topics</h2>
  <div class="dash"><b></b><i></i><i></i><i></i></div>
</div>
<a class="abs link-more" style="left:1023px;top:777px;font-size:12px;font-weight:500" href="#">See All Topics</a>
<div class="abs topics">
  <div class="topic" style="background:linear-gradient(180deg,#e9e3dc,#cdbfae)" role="img" aria-label="Tabby kitten standing on hind legs"><div class="shade"></div><span class="display">Sunbeam Policy</span></div>
  <div class="topic" style="background:linear-gradient(180deg,#8c8c82,#c7c3b8)" role="img" aria-label="Tabby cat resting beside a plant"><div class="shade"></div><span class="display">Catnip Economy</span></div>
  <div class="topic" style="background:radial-gradient(circle at 55% 40%,#5c4a3f,#1e1715)" role="img" aria-label="Dark grey cat in low light"><div class="shade"></div><span class="display">Moonlit Arts</span></div>
  <div class="topic" style="background:linear-gradient(180deg,#d8d4cf,#a9a39d)" role="img" aria-label="White and tabby kitten lying down"><div class="shade"></div><span class="display">Kitten Schools</span></div>
</div>

<!-- latest articles -->
<div class="abs center" style="left:0;width:1200px;top:1320px;text-align:center">
  <h2 class="section-title display">Latest Articles</h2>
  <div class="dash"><b></b><i></i><i></i><i></i></div>
</div>

<div class="abs articles">
  <article class="article">
    <div class="photo" style="background:radial-gradient(circle at 55% 55%,#c8692a,#6a3718 60%,#2c170c)" role="img" aria-label="Ginger cat lying on its side">
      <div class="stats"><span><svg width="9" height="9" viewBox="0 0 10 10" fill="none" stroke="#fff" stroke-width="1.2"><path d="M5 1a4 4 0 1 0 1.8 7.6L9 9l-.5-2A4 4 0 0 0 5 1z"/></svg>25</span><span><svg width="8" height="10" viewBox="0 0 8 10" fill="none" stroke="#fff" stroke-width="1.2"><path d="M4 1C5 3 7 4 7 6.5A3 3 0 0 1 1 6.5C1 5 2 4 2.5 3 3 4 3.5 4 4 1z"/></svg>150</span><span><svg width="9" height="9" viewBox="0 0 10 10" fill="none" stroke="#fff" stroke-width="1.2"><circle cx="5" cy="5" r="4"/><path d="M5 2.6V5l1.6 1"/></svg>3</span></div>
    </div>
    <div class="cats">POLITICS<i>|</i>ENVIRONMENT</div>
    <h3 class="display">Velurindale pledges clean rivers for every whiskered citizen</h3>
    <div class="byline"><span class="avatar"></span>BY ALICE • APRIL 10, 2025</div>
    <p class="excerpt">The Whisker Council voted softly but firmly to protect every stream, so that no paw need ever touch murky water again. Fish families welcomed the news.</p>
    <a class="link-more" href="#">Read More</a>
  </article>
  <article class="article">
    <div class="photo" style="background:linear-gradient(160deg,#a9c95a 0%,#6f9340 50%,#8a8f86 100%)" role="img" aria-label="Two grey tabby kittens outdoors">
      <div class="stats"><span><svg width="9" height="9" viewBox="0 0 10 10" fill="none" stroke="#fff" stroke-width="1.2"><path d="M5 1a4 4 0 1 0 1.8 7.6L9 9l-.5-2A4 4 0 0 0 5 1z"/></svg>25</span><span><svg width="8" height="10" viewBox="0 0 8 10" fill="none" stroke="#fff" stroke-width="1.2"><path d="M4 1C5 3 7 4 7 6.5A3 3 0 0 1 1 6.5C1 5 2 4 2.5 3 3 4 3.5 4 4 1z"/></svg>150</span><span><svg width="9" height="9" viewBox="0 0 10 10" fill="none" stroke="#fff" stroke-width="1.2"><circle cx="5" cy="5" r="4"/><path d="M5 2.6V5l1.6 1"/></svg>3</span></div>
    </div>
    <div class="cats">EDUCATION<i>|</i>COMMUNITY</div>
    <h3 class="display">Free nap halls open in every meadow village this spring</h3>
    <div class="byline"><span class="avatar"></span>BY ALICE • APRIL 10, 2025</div>
    <p class="excerpt">Kittens of every coat may now rest, read and learn side by side. Elders say shared cushions build kinder neighbours and calmer, curious minds.</p>
    <a class="link-more" href="#">Read More</a>
  </article>
  <article class="article">
    <div class="photo" style="background:linear-gradient(135deg,#e7e2dc 0%,#c98d67 45%,#b83a33 100%)" role="img" aria-label="Person in a red top hugging a cat">
      <div class="stats"><span><svg width="9" height="9" viewBox="0 0 10 10" fill="none" stroke="#fff" stroke-width="1.2"><path d="M5 1a4 4 0 1 0 1.8 7.6L9 9l-.5-2A4 4 0 0 0 5 1z"/></svg>25</span><span><svg width="8" height="10" viewBox="0 0 8 10" fill="none" stroke="#fff" stroke-width="1.2"><path d="M4 1C5 3 7 4 7 6.5A3 3 0 0 1 1 6.5C1 5 2 4 2.5 3 3 4 3.5 4 4 1z"/></svg>150</span><span><svg width="9" height="9" viewBox="0 0 10 10" fill="none" stroke="#fff" stroke-width="1.2"><circle cx="5" cy="5" r="4"/><path d="M5 2.6V5l1.6 1"/></svg>3</span></div>
    </div>
    <div class="cats">WORLD<i>|</i>DIPLOMACY</div>
    <h3 class="display">Border watch reports robot rats massing near Quendrosa</h3>
    <div class="byline"><span class="avatar"></span>BY ALICE • APRIL 10, 2025</div>
    <p class="excerpt">Scouts saw General Pikewhistle's clattering hamster columns at dusk. Our envoys answered with an open letter, a warm basket and calls for peace.</p>
    <a class="link-more" href="#">Read More</a>
  </article>
  <article class="article">
    <div class="photo" style="background:radial-gradient(circle at 50% 55%,#e9d7c4,#c78a54 55%,#8a5a36)" role="img" aria-label="Close-up of a calico cat">
      <div class="stats"><span><svg width="9" height="9" viewBox="0 0 10 10" fill="none" stroke="#fff" stroke-width="1.2"><path d="M5 1a4 4 0 1 0 1.8 7.6L9 9l-.5-2A4 4 0 0 0 5 1z"/></svg>25</span><span><svg width="8" height="10" viewBox="0 0 8 10" fill="none" stroke="#fff" stroke-width="1.2"><path d="M4 1C5 3 7 4 7 6.5A3 3 0 0 1 1 6.5C1 5 2 4 2.5 3 3 4 3.5 4 4 1z"/></svg>150</span><span><svg width="9" height="9" viewBox="0 0 10 10" fill="none" stroke="#fff" stroke-width="1.2"><circle cx="5" cy="5" r="4"/><path d="M5 2.6V5l1.6 1"/></svg>3</span></div>
    </div>
    <div class="cats">HEALTH<i>|</i>SCIENCE</div>
    <h3 class="display">Healers share a new remedy for the common hairball</h3>
    <div class="byline"><span class="avatar"></span>BY ALICE • APRIL 10, 2025</div>
    <p class="excerpt">A gentle brew of meadow grass and warm milk is now free at every clinic. Doctors hope all whiskered folk, young and old, will purr a little easier.</p>
    <a class="link-more" href="#">Read More</a>
  </article>
</div>

<a class="abs btn" style="left:518px;top:2825px;width:165px;height:47px" href="#">View All</a>
<div class="abs divider"></div>

<!-- featured posts -->
<div class="abs" style="left:85px;top:3008px">
  <h2 class="section-title display">Featured Posts</h2>
  <div class="dash"><b></b><i></i><i></i><i></i></div>
</div>
<a class="abs link-more" style="left:1059px;top:3023px" href="#">View All</a>
<div class="abs card-row" style="top:3096px">
  <article class="post">
    <div class="photo" style="background:linear-gradient(135deg,#d9c7ad 0%,#c88a4a 55%,#8a3d33 100%)" role="img" aria-label="Two cats resting on a checked blanket"></div>
    <div class="meta">BY ALICE • APRIL 10, 2025</div>
    <h3 class="display">Sisters share one blanket in winter warmth drive</h3>
    <p>Shelters ask every household to fold one spare quilt for a stray this cold season.</p>
    <a class="btn" href="#">Read More</a>
  </article>
  <article class="post">
    <div class="photo" style="background:linear-gradient(160deg,#e8ece6 0%,#9eb08c 50%,#6f8aa6 100%)" role="img" aria-label="Woman outdoors holding a cat"></div>
    <div class="meta">BY ALICE • APRIL 10, 2025</div>
    <h3 class="display">Garden guilds plant ten thousand catnip beds</h3>
    <p>Volunteers turned empty lots into green rest spots, open to every paw in the city.</p>
    <a class="btn" href="#">Read More</a>
  </article>
  <article class="post">
    <div class="photo" style="background:linear-gradient(135deg,#f0e8e0 0%,#d19a62 50%,#efe6dc 100%)" role="img" aria-label="Fluffy ginger and white cat lying on a bed"></div>
    <div class="meta">BY ALICE • APRIL 10, 2025</div>
    <h3 class="display">The quiet art of the long afternoon nap</h3>
    <p>Our columnist argues that rest is not idleness, but a gentle kind of courage.</p>
    <a class="btn" href="#">Read More</a>
  </article>
</div>

<!-- explore by topic -->
<div class="abs explore-band"></div>
<div class="abs center" style="left:0;width:1200px;top:3771px;text-align:center">
  <h2 class="section-title display">Explore By Topic</h2>
  <div class="dash"><b></b><i></i><i></i><i></i></div>
</div>
<a class="abs link-more" style="left:1059px;top:3786px" href="#">View All</a>
<div class="abs card-row" style="top:3859px">
  <article class="post">
    <div class="photo" style="background:linear-gradient(135deg,#c9c4bc 0%,#7d6f63 55%,#3f3a36 100%)" role="img" aria-label="Young man holding a long-haired cat"></div>
    <div class="meta">BY ALICE • APRIL 10, 2025</div>
    <h3 class="display">Refugee kittens find homes across the valley</h3>
    <p>Families from the borderlands were welcomed with open doors and warm saucers.</p>
    <a class="link-more" href="#">Read More</a>
  </article>
  <article class="post">
    <div class="photo" style="background:radial-gradient(circle at 55% 45%,#6e5a4a,#1a1614 70%)" role="img" aria-label="Two cats side by side on a dark background"></div>
    <div class="meta">BY ALICE • APRIL 10, 2025</div>
    <h3 class="display">Moonlight poets gather for the spring readings</h3>
    <p>Soft verses about friendship and fish drew the largest crowd in many seasons.</p>
    <a class="link-more" href="#">Read More</a>
  </article>
  <article class="post">
    <div class="photo" style="background:linear-gradient(135deg,#c8652f 0%,#8a4a30 50%,#4c3a33 100%)" role="img" aria-label="Man holding a grey and white cat"></div>
    <div class="meta">BY ALICE • APRIL 10, 2025</div>
    <h3 class="display">New fair-wage law for the mouse-catching trade</h3>
    <p>Workers cheered as the council promised rest days and a share of every catch.</p>
    <a class="link-more" href="#">Read More</a>
  </article>
</div>

<!-- newsletter -->
<section class="abs newsletter">
  <h2 class="display">Subscribe to our newsletter<br>and stay curled up &amp; informed</h2>
  <div class="subscribe">
    <div class="field"><svg width="12" height="9" viewBox="0 0 12 9" fill="none" stroke="#8a8c99" stroke-width="1.1"><rect x=".5" y=".5" width="11" height="8" rx="1"/><path d="M1 1l5 4 5-4"/></svg>Your email address</div>
    <div class="send">Subscribe</div>
  </div>
</section>

<!-- footer -->
<div class="abs foot-logo display">Velurindale</div>
<p class="abs foot-about">Gentle news for curious whiskers, written by cats, for cats, from the heart of the valley.</p>
<div class="abs copy">© 2025 <b>Velurindale</b>. All right reserved.</div>
<div class="abs stamp">April 8, 2025. Layout_4</div>

<div class="abs foot-col" style="left:466px;top:4782px">
  <h4>Quick Links</h4><div class="dash"><b></b><i></i><i></i><i></i></div>
  <ul><li>Home</li><li>Archives</li><li>Posts</li><li>Post Format</li><li>Pages</li></ul>
</div>
<div class="abs foot-col" style="left:655px;top:4782px">
  <h4>Category</h4><div class="dash"><b></b><i></i><i></i><i></i></div>
  <ul><li>Politics</li><li>Purr Arts</li><li>Sunbeam Science</li><li>Kitten Life</li></ul>
</div>
<div class="abs foot-col" style="left:850px;top:4782px">
  <h4>Follow Us</h4><div class="dash"><b></b><i></i><i></i><i></i></div>
</div>
<div class="abs follow">
  <a href="#"><i></i>Friendgrid</a>
  <a href="#"><i></i>Chirpline</a>
  <a href="#"><i></i>Snapframe</a>
  <a href="#"><i></i>Clipstream</a>
</div>

</body>
</html>
```